Retail swing tag labels for a sale / reduction

We need some graphics done to be made into retail swing tag labels, for the purpose of reductions on selected products.

We have attached 2 examples of previous designs that were similar idea, but more themed for 'autumn' and 'winter'. This theme will just have the word 'REDUCED'.

The white areas can be smaller in size, as we would like to include a large "20% OFF" at the bottom, and then a 30%, 40%, 50% option.

Overall colour scheme should be red background with some form of detailed patterning (see previous examples). Bright and e-catching.

Any other questions, just ask.

The screenshot is front the printers, but in horizontal orientation.

The finished dimensions will be A6 portrait, printed both sides.

We have also included the vector file of the shop "Hollowbrook Emporium", which can be included on 1 of the sides.

```html
<!DOCTYPE html>
<html lang="en">
<head>
<meta charset="utf-8">
<title>Hollowbrook Emporium – Reduced Swing Tag</title>
<link rel="stylesheet" href="https://fonts.googleapis.com/css2?family=Poppins:wght@400;700&display=swap">
<style>
  :root {
    --page-bg: #ffffff;
    --tag-bg: #ffffff;
    --sale-top: #d7192b;
    --sale-mid: #c41424;
    --sale-bottom: #9c0f1c;
    --sale-fleck: rgba(255, 255, 255, 0.22);
    --sale-fleck-soft: rgba(255, 255, 255, 0.10);
    --brand-red: #b5121f;
    --label-white: #ffffff;
  }
  html, body {
    margin: 0;
    padding: 0;
    width: 1200px;
    height: 1200px;
    overflow: hidden;
    background: var(--page-bg);
  }
  .canvas {
    position: relative;
    width: 1200px;
    height: 1200px;
  }
  .swing-tag {
    position: absolute;
    left: 311px;
    top: 222px;
    width: 585px;
    height: 834px;
    background: var(--tag-bg);
    overflow: hidden;
    font-family: "Poppins", sans-serif;
  }
  .sale-scene {
    position: absolute;
    left: 0;
    top: 0;
    width: 585px;
    height: 480px;
    background:
      radial-gradient(circle, var(--sale-fleck) 0 3px, transparent 4px) 0 0 / 46px 46px,
      radial-gradient(circle, var(--sale-fleck-soft) 0 6px, transparent 7px) 23px 23px / 46px 46px,
      linear-gradient(180deg, var(--sale-top) 0%, var(--sale-mid) 50%, var(--sale-bottom) 100%);
  }
  .reduced-label {
    position: absolute;
    left: 34px;
    top: 147px;
    width: 516px;
    height: 163px;
    background: var(--label-white);
    display: flex;
    align-items: center;
    justify-content: center;
  }
  .reduced-label h1 {
    margin: 0;
    font-weight: 700;
    font-size: 88px;
    line-height: 1;
    letter-spacing: 0.01em;
    color: var(--brand-red);
  }
  .discount {
    position: absolute;
    left: 0;
    top: 508px;
    width: 585px;
    margin: 0;
    text-align: center;
    font-weight: 700;
    font-size: 104px;
    line-height: 1.1;
    color: var(--brand-red);
    white-space: nowrap;
  }
  .brand {
    position: absolute;
    left: 0;
    top: 700px;
    width: 585px;
    display: flex;
    flex-direction: column;
    align-items: center;
    gap: 30px;
  }
  .brand-square {
    width: 18px;
    height: 18px;
    background: var(--brand-red);
  }
  .brand-name {
    margin: 0;
    font-weight: 400;
    font-size: 23px;
    letter-spacing: 0.2em;
    color: var(--brand-red);
    text-transform: uppercase;
    white-space: nowrap;
  }
</style>
</head>
<body>
  <div class="canvas">
    <article class="swing-tag">
      <div class="sale-scene" role="img" aria-label="Bright red seasonal backdrop with falling snow flecks"></div>
      <div class="reduced-label">
        <h1>REDUCED</h1>
      </div>
      <p class="discount">20% OFF</p>
      <footer class="brand">
        <span class="brand-square" aria-hidden="true"></span>
        <p class="brand-name">Hollowbrook Emporium</p>
      </footer>
    </article>
  </div>
</body>
</html>
```